Coral Bay Dental Surgery Business Cards

Hi there

Can i please have a simple business card designed (front and back with a black background) using out white reverse logo and the same font used for the logo?
On the back we can just have the logo. Full details at the front part.
Here are the details:

Name of the surgery: Coral Bay | Dental Surgery
Name on the business card: Dr Owen Thackery
Credentials:
BDSc (KTL)
MSc Oral Implantology (Halvorsen, Frankfurt)
Fellow & Diplomate (Meridian Council of Restorative Prosthetics)

Email: owen.thackery@coralbaysmile.example
Address: 17 Lisgrove Rd Karrinyup
Website: coralbaysmile.example
Phone: 1800 316 482

We have attached our high res logo and a rudimentary version of the business card which is not necessarily what we want but gives all the details
We would like to have the print ready version. Thanks.

Contact Information for Business Card

website. credentials. qr code. address. phone number

Requirements
Must have
• QR code

```html
<!DOCTYPE html>
<html lang="en">
<head>
<meta charset="utf-8">
<title>Coral Bay Dental Surgery – Business Cards</title>
<link href="https://fonts.googleapis.com/css2?family=Montserrat:wght@400;500;700&display=swap" rel="stylesheet">
<style>
  :root {
    --backdrop: #3a3a3a;
    --card: #1e1e1e;
    --card-edge: #2c2c2c;
    --ink: #f2f2f2;
    --ink-soft: #d6d6d6;
    --rule: #bdbdbd;
  }
  * { box-sizing: border-box; margin: 0; padding: 0; }
  html, body {
    width: 1200px; height: 758px; overflow: hidden;
    background: var(--backdrop);
    font-family: "Montserrat", sans-serif;
    color: var(--ink);
  }
  .sheet {
    width: 1200px; height: 758px;
    display: flex; align-items: center; justify-content: center; gap: 40px;
  }
  .card {
    position: relative;
    width: 540px; height: 310px;
    background: var(--card);
    border: 1px solid var(--card-edge);
    border-radius: 18px;
    overflow: hidden;
  }

  /* Back: name mark only */
  .card--back { display: flex; align-items: center; justify-content: center; }
  .brand { display: flex; align-items: center; gap: 18px; }
  .brand__dot {
    width: 58px; height: 58px; border-radius: 50%;
    border: 3px solid var(--ink); flex: none;
  }
  .brand__name {
    font-weight: 500; font-size: 30px; line-height: 1.15;
    letter-spacing: 0.06em; text-transform: uppercase; white-space: nowrap;
  }

  /* Front: details */
  .card--front { display: flex; align-items: stretch; padding: 30px 28px; }
  .front__brand {
    width: 160px; display: flex; flex-direction: column;
    justify-content: center; align-items: flex-start; gap: 12px;
  }
  .front__brand .brand__dot { width: 40px; height: 40px; border-width: 2px; }
  .front__brand .brand__name { font-size: 13.5px; letter-spacing: 0.04em; }
  .qr-code {
    width: 64px; height: 64px; margin-top: 4px;
    background: var(--ink); border-radius: 4px;
    border: 6px solid var(--ink);
    box-shadow: inset 0 0 0 3px var(--card);
  }
  .divider { width: 1px; background: var(--rule); margin: 6px 22px; flex: none; }
  .details { flex: 1; display: flex; flex-direction: column; justify-content: center; min-width: 0; }
  .details__name {
    font-weight: 700; font-size: 21px; letter-spacing: 0.02em;
    text-transform: uppercase; margin-bottom: 8px; white-space: nowrap;
  }
  .credentials { list-style: none; font-size: 10.5px; line-height: 1.5; color: var(--ink-soft); margin-bottom: 16px; }
  .contacts { list-style: none; font-size: 11.5px; }
  .contacts li { display: flex; align-items: center; gap: 9px; margin-bottom: 6px; white-space: nowrap; }
  .contacts svg { width: 17px; height: 17px; flex: none; }
</style>
</head>
<body>
<main class="sheet">

  <section class="card card--back" aria-label="Card back">
    <div class="brand">
      <span class="brand__dot"></span>
      <span class="brand__name">Coral Bay<br>Dental Surgery</span>
    </div>
  </section>

  <section class="card card--front" aria-label="Card front">
    <div class="front__brand">
      <span class="brand__dot"></span>
      <span class="brand__name">Coral Bay<br>Dental Surgery</span>
      <div class="qr-code" role="img" aria-label="QR code linking to the surgery website"></div>
    </div>
    <div class="divider"></div>
    <div class="details">
      <h1 class="details__name">Dr Owen Thackery</h1>
      <ul class="credentials">
        <li>BDSc (KTL)</li>
        <li>MSc Oral Implantology (Halvorsen, Frankfurt)</li>
        <li>Fellow &amp; Diplomate</li>
        <li>(Meridian Council of Restorative Prosthetics)</li>
      </ul>
      <ul class="contacts">
        <li>
          <svg viewBox="0 0 20 20" aria-hidden="true"><circle cx="10" cy="10" r="10" fill="var(--ink)"/><path d="M10 4.5a3.5 3.5 0 0 0-3.5 3.5c0 2.6 3.5 7 3.5 7s3.5-4.4 3.5-7A3.5 3.5 0 0 0 10 4.5z" fill="var(--card)"/><circle cx="10" cy="8" r="1.3" fill="var(--ink)"/></svg>
          17 Lisgrove Rd Karrinyup
        </li>
        <li>
          <svg viewBox="0 0 20 20" aria-hidden="true"><circle cx="10" cy="10" r="10" fill="var(--ink)"/><path d="M6.5 5h2l1 2.5-1.3 1a6 6 0 0 0 3.3 3.3l1-1.3 2.5 1v2a1 1 0 0 1-1 1A8 8 0 0 1 5.5 6a1 1 0 0 1 1-1z" fill="var(--card)"/></svg>
          1800 316 482
        </li>
        <li>
          <svg viewBox="0 0 20 20" aria-hidden="true"><circle cx="10" cy="10" r="10" fill="var(--ink)"/><rect x="5" y="6.5" width="10" height="7" rx="1" fill="var(--card)"/><path d="M5.5 7l4.5 3.5L14.5 7" stroke="var(--ink)" stroke-width="1" fill="none"/></svg>
          owen.thackery@coralbaysmile.example
        </li>
        <li>
          <svg viewBox="0 0 20 20" aria-hidden="true"><circle cx="10" cy="10" r="10" fill="var(--ink)"/><circle cx="10" cy="10" r="5" fill="none" stroke="var(--card)" stroke-width="1.2"/><ellipse cx="10" cy="10" rx="2.2" ry="5" fill="none" stroke="var(--card)" stroke-width="1"/><path d="M5 10h10" stroke="var(--card)" stroke-width="1"/></svg>
          www.coralbaysmile.example
        </li>
      </ul>
    </div>
  </section>

</main>
</body>
</html>
```